Bright Nook Home Page (A Home Wellness e-commerce site & blog)

We need a dynamic home page created for a home wellness brand. Must be visually appealing and extremely mobile-friendly. Logos and a Navmap have been provided but that is just a guideline, PLEASE USE YOUR CREATIVITY.

Target Market(s)

1st target demo: females 24-48, 2nd target demo: all 24-48

Number of Pages Required

1 page

```html
<!DOCTYPE html>
<html lang="en">
<head>
<meta charset="utf-8">
<title>Bright Nook – Home Wellness</title>
<link href="https://fonts.googleapis.com/css2?family=Roboto:wght@300;400;500;700;900&display=swap" rel="stylesheet">
<style>
:root{
  --purple:#4f2d91;
  --purple-deep:#3f2178;
  --teal:#3cc4cf;
  --ink:#2a2a2a;
  --muted:#555;
  --footer:#1b1b1d;
  --white:#fff;
}
*{box-sizing:border-box;margin:0;padding:0}
html,body{width:1200px;height:2894px;overflow:hidden}
body{position:relative;font-family:'Roboto',sans-serif;color:var(--ink);background:var(--white)}
.abs{position:absolute}
a{color:inherit;text-decoration:none}

/* header */
.site-header{left:0;top:0;width:1200px;height:71px;background:var(--purple)}
.brand{left:129px;top:17px;font-size:32px;font-weight:500;color:var(--white);letter-spacing:-.5px}
.promo{left:638px;top:16px;font-size:11px;font-weight:500;color:var(--teal)}
.social-top{left:890px;top:17px;display:flex;gap:14px}
.social-top span{width:9px;height:9px;border-radius:50%;background:var(--white);display:block}
.nav{top:44px;font-size:13px;font-weight:500;color:var(--white)}
.nav.active{color:var(--teal);text-decoration:underline}
.cart{left:1011px;top:13px;width:61px;height:45px;background:var(--teal);border-radius:2px}
.cart svg{position:absolute;left:12px;top:11px}
.cart-count{position:absolute;left:36px;top:16px;width:14px;height:14px;border-radius:50%;background:var(--white);color:var(--teal);font-size:9px;font-weight:700;text-align:center;line-height:14px}

/* hero */
.hero{left:0;top:71px;width:1200px;height:414px;background:linear-gradient(100deg,#5b3a26 0%,#a77a58 25%,#caa183 45%,#8a5a3b 65%,#c9a98e 85%,#6c4b35 100%)}
.hero-title{left:127px;top:194px;font-size:37px;font-weight:900;color:var(--white)}
.hero-text{left:127px;top:245px;width:330px;font-size:13.5px;line-height:20px;color:var(--white)}
.btn{background:var(--purple);color:var(--white);font-weight:700;text-align:center;border-radius:2px}
.hero-btn{left:127px;top:315px;width:119px;height:33px;line-height:33px;font-size:13px}
.dot{top:459px;width:7px;height:7px;border-radius:50%;background:var(--purple)}
.dot.on{top:455px;width:14px;height:14px;border:2px solid var(--teal);background:var(--purple-deep)}

/* sale */
.sale{left:127px;top:542px;width:945px;height:188px;background:linear-gradient(90deg,#e6e6e8,#f2f2f3 45%,#e9e9ea)}
.sale-photo{left:598px;top:542px;width:474px;height:188px;background:linear-gradient(90deg,rgba(240,240,240,0),#d8d8d6 30%,#cfc9bb 70%,#d8c9a4)}
.ribbon{left:249px;top:579px}
.sale-big{left:261px;top:588px;width:205px;text-align:center;font-size:43px;font-weight:700;color:var(--white)}
.sale-sub{left:261px;top:637px;width:205px;text-align:center;font-size:14px;color:var(--white)}
.sale-line{left:171px;top:680px;font-size:20px;font-weight:300;color:#333}

/* section headings */
.sec-title{left:0;width:1200px;text-align:center;font-size:29px;font-weight:700;color:var(--purple)}
.smile{left:590px}
.sec-sub{left:0;width:1200px;text-align:center;font-size:13px;color:var(--ink)}

/* product grid */
.tile{width:238px}
.t1{left:222px;top:900px;height:237px;background:linear-gradient(135deg,#e0d6c6,#b88450 55%,#7a5a3c)}
.t2{left:481px;top:900px;height:237px;background:linear-gradient(135deg,#d8cbbd,#8c5a3c 50%,#c23a6a 80%,#eee)}
.t3{left:739px;top:900px;height:496px;background:linear-gradient(90deg,#efe6e0,#e8cfc4 50%,#ea8cc0 85%,#f3bedd)}
.t4{left:222px;top:1158px;height:238px;background:linear-gradient(135deg,#c8a584,#8b5a36 50%,#b98b62)}
.t5{left:481px;top:1158px;height:238px;background:linear-gradient(135deg,#a9b99a,#8c5a38 55%,#d8d8d0)}

/* about */
.about{left:0;top:1466px;width:1200px;height:363px;background:linear-gradient(90deg,#cfcfd1 0%,#eeeef0 22%,#f3f3f5 50%,#eeeef0 78%,#cfcfcf 100%)}
.about-copy{left:330px;width:540px;text-align:center;font-size:13px;line-height:17.5px;color:#222}
.about-btn{left:539px;top:1735px;width:122px;height:32px;line-height:32px;font-size:12px}

/* finance band */
.finance{left:127px;top:1900px;width:945px;height:189px;background:var(--purple)}
.finance-line{left:127px;top:1948px;width:945px;text-align:center;font-size:27px;color:var(--white)}
.finance-brand{left:520px;top:1993px;display:flex;align-items:center;gap:12px;font-size:40px;font-weight:500;color:var(--white)}
.finance-brand span.mark{width:38px;height:38px;border-radius:50%;background:var(--white);display:block}

/* blogs */
.blog-img{top:2250px;width:301px;height:188px}
.b1{left:127px;background:linear-gradient(135deg,#eaeaea,#cfcfcf 40%,#e5a3c4 80%)}
.b2{left:449px;background:linear-gradient(135deg,#3f8b9a,#c99b7e 45%,#e9e2dc 65%,#4b8f9e)}
.b3{left:771px;background:linear-gradient(135deg,#f1ece4,#e6b36a 45%,#f0883a 75%,#efe7dc)}
.blog-card{top:2416px;width:279px;height:123px;background:var(--white);box-shadow:0 4px 14px rgba(0,0,0,.07)}
.blog-num{position:absolute;left:16px;top:20px;font-size:27px;font-weight:700;color:var(--purple)}
.blog-date{position:absolute;left:15px;top:54px;font-size:9.5px;color:#666}
.blog-text{position:absolute;left:83px;top:20px;width:180px;font-size:14.5px;line-height:18px;color:#222}
.blog-link{position:absolute;left:83px;top:88px;font-size:11.5px;color:var(--teal);text-decoration:underline}

/* footer */
.footer{left:0;top:2610px;width:1200px;height:247px;background:var(--footer)}
.foot-brand{left:127px;top:2666px;font-size:32px;font-weight:500;color:var(--white)}
.foot-desc{left:127px;top:2726px;width:270px;font-size:11.5px;line-height:17px;color:#bbb}
.foot-social{left:127px;top:2787px;display:flex;gap:22px}
.foot-social span{width:12px;height:12px;border-radius:50%;background:var(--white);display:block}
.foot-social span.hi{background:var(--teal)}
.foot-head{top:2662px;font-size:16px;font-weight:500;color:var(--white)}
.foot-link{left:452px;font-size:11.5px;color:#ccc}
.contact{left:613px;font-size:11.5px;line-height:16px;color:#ddd}
.contact-icon{left:588px}
.news-input{left:828px;top:2699px;width:244px;height:35px;background:var(--white);border:1px solid #ccc;font-size:11px;color:#999;padding:11px 14px}
.news-btn{left:828px;top:2749px;width:130px;height:33px;line-height:33px;font-size:13px}
.chat{left:1098px;top:2789px;width:46px;height:46px;border-radius:50%;background:var(--teal)}
.chat svg{position:absolute;left:12px;top:13px}
.copyright{left:0;top:2857px;width:1200px;height:37px;background:var(--purple);color:var(--white);font-size:11.5px;text-align:center;line-height:37px}
</style>
</head>
<body>

<header class="abs site-header"></header>
<div class="abs brand">Bright Nook</div>
<div class="abs promo">Free shipping on all orders $50 and over!</div>
<div class="abs social-top" aria-label="Social links"><span></span><span></span><span></span><span></span></div>
<a class="abs nav active" style="left:597px">Home</a>
<a class="abs nav" style="left:669px">Product</a>
<a class="abs nav" style="left:752px">About Us</a>
<a class="abs nav" style="left:843px">Blogs</a>
<a class="abs nav" style="left:912px">Conatct Us</a>
<div class="abs cart">
  <svg width="20" height="22" viewBox="0 0 20 22" fill="none" stroke="#fff" stroke-width="1.8"><rect x="2" y="6" width="16" height="14" rx="1"/><path d="M6 9V5a4 4 0 0 1 8 0v4"/></svg>
  <span class="cart-count">0</span>
</div>

<section class="abs hero" role="img" aria-label="Photo of a woman receiving a relaxing face massage by candlelight"></section>
<h1 class="abs hero-title">Improve Your Body Today</h1>
<p class="abs hero-text">Lorem Ipsum is simply dummy text of the printing and typesetting industry. Lorem Ipsum...</p>
<a class="abs btn hero-btn">Shop Now</a>
<span class="abs dot" style="left:570px"></span>
<span class="abs dot" style="left:588px"></span>
<span class="abs dot on" style="left:602px"></span>
<span class="abs dot" style="left:623px"></span>

<section class="abs sale"></section>
<div class="abs sale-photo" role="img" aria-label="Photo of rolled white towels, candles, massage stones and oil bottle"></div>
<svg class="abs ribbon" width="229" height="90" viewBox="0 0 229 90"><polygon points="12,0 217,0 217,80 229,90 0,90 12,80" fill="#4f2d91"/><polygon points="0,90 12,80 12,90" fill="#2f1a5a"/><polygon points="229,90 217,80 217,90" fill="#2f1a5a"/></svg>
<div class="abs sale-big">50% OFF</div>
<div class="abs sale-sub">Sale going on Now!</div>
<div class="abs sale-line">Because saving money also makes us happy</div>

<h2 class="abs sec-title" style="top:793px">Featured Product</h2>
<svg class="abs smile" style="top:829px" width="20" height="7" viewBox="0 0 20 7"><path d="M1 1q9 8 18 0" fill="none" stroke="#3cc4cf" stroke-width="2"/></svg>
<p class="abs sec-sub" style="top:843px">The key to total bliss is nurturing the mind, body, and soul</p>

<div class="abs tile t1" role="img" aria-label="Product photo of an oil bottle in a wooden bowl"></div>
<div class="abs tile t2" role="img" aria-label="Product photo of a wooden massager with an orchid and towel"></div>
<div class="abs tile t3" role="img" aria-label="Beauty photo of a model with pink orchids"></div>
<div class="abs tile t4" role="img" aria-label="Product photo of a wooden tray with candle and blossoms"></div>
<div class="abs tile t5" role="img" aria-label="Product photo of bath salts, brush and oil on a tray"></div>

<section class="abs about" role="img" aria-label="Photo of white towels, soap and a teapot on a pale table"></section>
<h2 class="abs sec-title" style="top:1527px">About Us</h2>
<svg class="abs smile" style="top:1563px" width="20" height="7" viewBox="0 0 20 7"><path d="M1 1q9 8 18 0" fill="none" stroke="#3cc4cf" stroke-width="2"/></svg>
<p class="abs about-copy" style="top:1601px">They say that home is where the heart is. But home is also where your mind and body reside. At Bright Nook we believe that home should be your place of Zen.</p>
<p class="abs about-copy" style="top:1652px">A respite from the crazy world outside those walls. It is where you recharge your soul so you can approach each day with the focus and energy necessary to conquer the world.</p>
<a class="abs btn about-btn">Tell Me More</a>

<section class="abs finance"></section>
<p class="abs finance-line">Don’t sweat it. You can pay later.</p>
<div class="abs finance-brand"><span class="mark"></span>Crumb Pay</div>

<h2 class="abs sec-title" style="top:2152px">The Happy Blogs</h2>
<svg class="abs smile" style="top:2188px" width="20" height="7" viewBox="0 0 20 7"><path d="M1 1q9 8 18 0" fill="none" stroke="#3cc4cf" stroke-width="2"/></svg>
<p class="abs sec-sub" style="top:2201px">Food for the mind, tips for the body and exercises for the soul</p>

<div class="abs blog-img b1" role="img" aria-label="Photo of a towel, lotion bottle and pink tulips"></div>
<div class="abs blog-img b2" role="img" aria-label="Photo of a woman enjoying a spa massage"></div>
<div class="abs blog-img b3" role="img" aria-label="Photo of oil bottles, soap and an orange"></div>

<article class="abs blog-card" style="left:138px">
  <span class="blog-num">04</span><span class="blog-date">May, 21</span>
  <p class="blog-text">Lorem Ipsum is simply dummy text of the printing industry.</p>
  <a class="blog-link">Explore More</a>
</article>
<article class="abs blog-card" style="left:460px">
  <span class="blog-num">03</span><span class="blog-date">May, 21</span>
  <p class="blog-text">Lorem Ipsum is simply dummy text of the printing industry.</p>
  <a class="blog-link">Explore More</a>
</article>
<article class="abs blog-card" style="left:782px">
  <span class="blog-num">01</span><span class="blog-date">May, 21</span>
  <p class="blog-text">Lorem Ipsum is simply dummy text of the printing industry.</p>
  <a class="blog-link">Explore More</a>
</article>

<footer class="abs footer"></footer>
<div class="abs foot-brand">Bright Nook</div>
<p class="abs foot-desc">Lorem Ipsum is simply dummy text of the printing and typesetting industry. Lorem Ipsum...</p>
<div class="abs foot-social" aria-label="Social links"><span></span><span></span><span class="hi"></span><span></span></div>

<h3 class="abs foot-head" style="left:452px">Quick Link</h3>
<a class="abs foot-link" style="top:2696px">Home</a>
<a class="abs foot-link" style="top:2719px">Product</a>
<a class="abs foot-link" style="top:2742px">About Us</a>
<a class="abs foot-link" style="top:2766px">Blogs</a>
<a class="abs foot-link" style="top:2790px">Conatct Us</a>

<h3 class="abs foot-head" style="left:587px">Conatct info</h3>
<svg class="abs contact-icon" style="top:2695px" width="12" height="16" viewBox="0 0 12 16"><path d="M6 0a6 6 0 0 0-6 6c0 4.5 6 10 6 10s6-5.5 6-10a6 6 0 0 0-6-6z" fill="#3cc4cf"/><circle cx="6" cy="6" r="2.3" fill="#1b1b1d"/></svg>
<p class="abs contact" style="top:2696px">lorem ipsum, 88 Harbour Lane<br>Millbrook, NL &nbsp;A2B 3C4</p>
<svg class="abs contact-icon" style="top:2749px" width="13" height="13" viewBox="0 0 24 24"><path d="M6.6 10.8a15 15 0 0 0 6.6 6.6l2.2-2.2a1 1 0 0 1 1-.25 11.4 11.4 0 0 0 3.6.6 1 1 0 0 1 1 1V20a1 1 0 0 1-1 1A17 17 0 0 1 3 4a1 1 0 0 1 1-1h3.5a1 1 0 0 1 1 1c0 1.25.2 2.45.6 3.6a1 1 0 0 1-.25 1z" fill="#3cc4cf"/></svg>
<p class="abs contact" style="top:2748px">555.210.0147</p>
<svg class="abs contact-icon" style="top:2785px" width="14" height="10" viewBox="0 0 14 10"><rect x="0.5" y="0.5" width="13" height="9" fill="none" stroke="#3cc4cf"/><path d="M0.5 0.5l6.5 5 6.5-5" fill="none" stroke="#3cc4cf"/></svg>
<p class="abs contact" style="top:2782px">info@brightnook.com</p>

<h3 class="abs foot-head" style="left:827px">Sign up for our Newsletter</h3>
<div class="abs news-input">enter your email address here...</div>
<a class="abs btn news-btn">Subscribe Now!</a>

<div class="abs chat">
  <svg width="22" height="20" viewBox="0 0 22 20"><rect x="1" y="1" width="20" height="15" rx="4" fill="#fff"/><path d="M5 16l-2 3 6-3z" fill="#fff"/><rect x="6" y="6" width="10" height="1.8" fill="#3cc4cf"/><rect x="6" y="10" width="10" height="1.8" fill="#3cc4cf"/></svg>
</div>

<div class="abs copyright">Copyright © 2021 Bright Nook. All Rights Reserved</div>

</body>
</html>
```